Food company business card needs a freshen up

A little bit about our business. Wholesale Food Company (Vela Nu PNG Ltd) with a number of retail businesses including a Deli Butchery/Bakery (named The Bova Grill Yard) and Fast-Food Restaurants (Condor Wraps, Tam Lok Ret, Reefies) and a catering company called Bova Lulu Catering. At our head office (Vela Nu) we also have 2 manufacturing factories - Bakery (Bova Oven Loft products) and Butchery (Bova Fine products). We are proudly 100% PNG owned - this could be good to include somewhere on the business card.
Our current website is:
www.vnq-sample.com.pg
Please visit our website for further design aesthetics that we would like to tie into our business cards and information can be found on our website. Colour schemes are red, black and white.
We have a previous draft business card (attached) that we want to be improved to match our new website aesthetics.
We would like to make the business cards portrait and individualised for each of our staff members that require them and would like these to be editable to change the details when needed. We want these to be modern, professional and visually engaging with the use of photos (stock images used in our draft). If we can get photos of meat/sausages, fresh uncooked chicken, fresh fish, potato fries, cheese burger, bread roll/pies, and vegetables (make it look green and fresh) – these should be generic photos and product focused.
Constant information we want to see on the business cards.
1. Vela Nu PNG LTD
- Wholesale Food Sales & Delivery
- Butchery Manufacturing
- Bakery Manufacturing
- Quality Assurance
- Customs & Freight
- Retail
- Catering & Equipment Hire
2. Website – www.vnq-sample.com.pg
3. Phone – 345 6710 / 345 6722
4. Address – Sec 212, Lot 8. Kewana Rd, Tatuna
5. And logos of all our retail brands.
I have attached each of our logos. I have also attached a tribal fish design which we use on all business cards, email signatures and uniforms across all sites.
- Vela Nu Logo
- Grill Yard Logo
- Condor Wraps Logo
- Reefies Logo
- Tam Lok Ret Logo
- Bova Lulu Catering Logo
- Oven Loft Logo (for Vela Nu - Bakery Factory Products)
- Bova Fine logo (for Vela Nu - Butchery Factory Products)
- QSVER logo (Quality Assurance cert of our Butchery Factory)
Information that will change:
Name – e.g. Peter Olo
Title – Marketing & Promotions
Email –peterolo@velanusample.com.pg
Mobile – (+675 7222 2222)
Please use Peter Olo as an example in your designs.
Thank you and looking forward to your designs :)
Miriam
Target Market(s)
Local and International Clients
Industry/Entity Type
Food Industry
Contact Information for Business Card
See detailed brief

```html
<!DOCTYPE html>
<html lang="en">
<head>
<meta charset="utf-8">
<title>Vela Nu PNG Ltd – Portrait Business Card</title>
<link rel="stylesheet" href="https://fonts.googleapis.com/css2?family=Arimo:wght@400;700&display=swap">
<style>
  :root {
    --bg: #dcdcdc;
    --card: #f7f7f7;
    --red: #e03c31;
    --black: #1c1c1c;
    --white: #ffffff;
    --grey: #5a5a5a;
    --green: #4aa12c;
    --blue: #1f4fa0;
    --teal: #2a9d8f;
    --brown: #7a4a22;
    --deep-red: #b3171c;
  }
  * { box-sizing: border-box; margin: 0; padding: 0; }
  html, body { width: 1200px; height: 800px; overflow: hidden; }
  body {
    background: var(--bg);
    font-family: "Arimo", Arial, sans-serif;
    position: relative;
  }
  .card {
    position: absolute;
    top: 120px;
    width: 340px;
    height: 560px;
    border-radius: 20px;
    background: var(--card);
    overflow: hidden;
    box-shadow: 0 6px 16px rgba(0,0,0,0.18);
  }
  .card--front { left: 220px; }
  .card--back { left: 640px; }

  /* company name block */
  .brand {
    display: flex;
    align-items: center;
    justify-content: center;
    gap: 8px;
    font-weight: 700;
    color: var(--black);
    white-space: nowrap;
  }
  .brand__dot { width: 13px; height: 13px; border-radius: 50%; background: var(--red); flex: none; }
  .brand__name { font-size: 34px; }
  .brand__suffix { font-size: 14px; }
  .tagline {
    text-align: center;
    font-size: 11px;
    letter-spacing: 2px;
    text-transform: uppercase;
    color: var(--grey);
    margin-top: 4px;
  }

  /* photo strips */
  .photos {
    position: absolute;
    left: 0; width: 100%;
    display: flex;
  }
  .photo { flex: 1; height: 100%; }
  .photo--meat { background: linear-gradient(160deg, #b33a2e, #7a1f1a); }
  .photo--chicken { background: linear-gradient(160deg, #f2d4bf, #d9a88a); }
  .photo--fish { background: linear-gradient(160deg, #9fb8c4, #5d7f8f); }
  .photo--veg { background: linear-gradient(160deg, #7cc04a, #2f7d23); }
  .photo--fries { background: linear-gradient(160deg, #f3c24a, #d48a1c); }
  .photo--burger { background: linear-gradient(160deg, #c98a44, #6b3a1e); }
  .photo--bread { background: linear-gradient(160deg, #e6b97a, #a8692e); }

  /* front */
  .card--front .brand-block { position: absolute; top: 34px; left: 0; width: 100%; }
  .card--front .photos { top: 118px; height: 130px; }
  .front-band { position: absolute; left: 0; top: 0; width: 100%; height: 100%; }

  .holder {
    position: absolute;
    left: 30px; top: 318px; right: 30px;
    color: var(--white);
    padding-bottom: 12px;
    border-bottom: 1px solid rgba(255,255,255,0.75);
  }
  .holder__name { font-size: 26px; font-weight: 700; }
  .holder__title { font-size: 14px; margin-top: 4px; }

  .contacts {
    position: absolute;
    left: 30px; top: 400px; right: 20px;
    list-style: none;
    color: var(--white);
    font-size: 13px;
    line-height: 1.75;
  }
  .contacts li { display: flex; align-items: center; gap: 10px; white-space: nowrap; }
  .contacts svg { width: 13px; height: 13px; flex: none; }

  /* back */
  .card--back .photos { top: 0; height: 96px; }
  .card--back .brand-block { position: absolute; top: 112px; left: 0; width: 100%; }
  .card--back .brand__name { font-size: 28px; }
  .card--back .brand__suffix { font-size: 12px; }

  .services {
    position: absolute;
    left: 34px; top: 172px; right: 24px;
    list-style: none;
    font-size: 13px;
    line-height: 20px;
    color: var(--black);
  }
  .services li { display: flex; align-items: center; gap: 9px; }
  .services svg { width: 11px; height: 11px; flex: none; }

  .brands {
    position: absolute;
    left: 24px; right: 24px; top: 330px;
    border-top: 1px solid #cfcfcf;
    padding-top: 12px;
    display: grid;
    grid-template-columns: 1fr 1fr;
    row-gap: 8px;
    column-gap: 10px;
  }
  .partner { font-size: 15px; font-weight: 700; white-space: nowrap; height: 22px; line-height: 22px; }
  .partner--grill { color: var(--red); }
  .partner--wraps { color: var(--blue); }
  .partner--pie { color: var(--green); }
  .partner--reef { color: var(--teal); }
  .partner--lulu { color: var(--black); }
  .partner--fine { color: var(--deep-red); }
  .partner--loft { color: var(--brown); }
  .cert-badge { width: 60px; height: 22px; border-radius: 4px; background: var(--black); }

  .back-footer {
    position: absolute;
    left: 0; bottom: 0; width: 100%; height: 62px;
    background: var(--red);
    border-top: 6px solid var(--black);
    color: var(--white);
    display: flex;
    flex-direction: column;
    align-items: center;
    justify-content: center;
    gap: 3px;
  }
  .back-footer__owned { font-size: 15px; font-weight: 700; letter-spacing: 1px; }
  .back-footer__web { font-size: 12px; }
</style>
</head>
<body>

<section class="card card--front" aria-label="Business card front">
  <div class="brand-block">
    <div class="brand"><span class="brand__dot"></span><span class="brand__name">Vela Nu</span><span class="brand__suffix">PNG LTD</span></div>
    <p class="tagline">Wholesale Food Company</p>
  </div>

  <div class="photos">
    <div class="photo photo--meat" role="img" aria-label="Photo of fresh meat and sausages"></div>
    <div class="photo photo--chicken" role="img" aria-label="Photo of fresh uncooked chicken"></div>
    <div class="photo photo--fish" role="img" aria-label="Photo of fresh fish"></div>
    <div class="photo photo--veg" role="img" aria-label="Photo of fresh green vegetables"></div>
  </div>

  <svg class="front-band" viewBox="0 0 340 560" preserveAspectRatio="none" aria-hidden="true">
    <path d="M0 248 L340 248 L340 252 C 240 262, 110 278, 0 300 Z" fill="var(--card)"/>
    <path d="M0 292 C 110 270, 240 254, 340 244 L340 258 C 240 268, 110 284, 0 306 Z" fill="var(--black)"/>
    <path d="M0 312 C 110 290, 240 274, 340 264 L340 560 L0 560 Z" fill="var(--red)"/>
  </svg>

  <div class="holder">
    <p class="holder__name">Peter Olo</p>
    <p class="holder__title">Marketing &amp; Promotions</p>
  </div>

  <ul class="contacts">
    <li>
      <svg viewBox="0 0 12 12"><path d="M2 1 L4.5 1 L5.5 3.5 L4 4.5 C4.7 6 6 7.3 7.5 8 L8.5 6.5 L11 7.5 L11 10 C6 10.5 1.5 6 2 1 Z" fill="var(--white)"/></svg>
      345 6710 / 345 6722
    </li>
    <li>
      <svg viewBox="0 0 12 12"><rect x="3" y="0.8" width="6" height="10.4" rx="1" fill="none" stroke="var(--white)" stroke-width="1.2"/></svg>
      +675 7222 2222
    </li>
    <li>
      <svg viewBox="0 0 12 12"><rect x="0.8" y="2.2" width="10.4" height="7.6" rx="1" fill="var(--white)"/><path d="M1 3 L6 7 L11 3" fill="none" stroke="var(--red)" stroke-width="1.1"/></svg>
      peterolo@velanusample.com.pg
    </li>
    <li>
      <svg viewBox="0 0 12 12"><circle cx="6" cy="6" r="5.2" fill="var(--white)"/><path d="M1 6 H11 M6 1 C3.5 4 3.5 8 6 11 M6 1 C8.5 4 8.5 8 6 11" fill="none" stroke="var(--red)" stroke-width="0.9"/></svg>
      www.vnq-sample.com.pg
    </li>
    <li>
      <svg viewBox="0 0 12 12"><path d="M6 11.5 C 3 7.5, 2 6, 2 4.3 A4 4 0 0 1 10 4.3 C 10 6, 9 7.5, 6 11.5 Z" fill="var(--white)"/><circle cx="6" cy="4.4" r="1.5" fill="var(--red)"/></svg>
      Sec 212, Lot 8. Kewana Rd, Tatuna
    </li>
  </ul>
</section>

<section class="card card--back" aria-label="Business card back with services and retail brands">
  <div class="photos">
    <div class="photo photo--fries" role="img" aria-label="Photo of potato fries"></div>
    <div class="photo photo--burger" role="img" aria-label="Photo of a cheeseburger"></div>
    <div class="photo photo--bread" role="img" aria-label="Photo of bread rolls and pies"></div>
  </div>

  <div class="brand-block">
    <div class="brand"><span class="brand__dot"></span><span class="brand__name">Vela Nu</span><span class="brand__suffix">PNG LTD</span></div>
  </div>

  <ul class="services">
    <li><svg viewBox="0 0 12 12"><path d="M1.5 6.5 L4.5 9.5 L10.5 2.5" fill="none" stroke="var(--red)" stroke-width="2"/></svg>Wholesale Food Sales &amp; Delivery</li>
    <li><svg viewBox="0 0 12 12"><path d="M1.5 6.5 L4.5 9.5 L10.5 2.5" fill="none" stroke="var(--red)" stroke-width="2"/></svg>Butchery Manufacturing</li>
    <li><svg viewBox="0 0 12 12"><path d="M1.5 6.5 L4.5 9.5 L10.5 2.5" fill="none" stroke="var(--red)" stroke-width="2"/></svg>Bakery Manufacturing</li>
    <li><svg viewBox="0 0 12 12"><path d="M1.5 6.5 L4.5 9.5 L10.5 2.5" fill="none" stroke="var(--red)" stroke-width="2"/></svg>Quality Assurance</li>
    <li><svg viewBox="0 0 12 12"><path d="M1.5 6.5 L4.5 9.5 L10.5 2.5" fill="none" stroke="var(--red)" stroke-width="2"/></svg>Customs &amp; Freight</li>
    <li><svg viewBox="0 0 12 12"><path d="M1.5 6.5 L4.5 9.5 L10.5 2.5" fill="none" stroke="var(--red)" stroke-width="2"/></svg>Retail</li>
    <li><svg viewBox="0 0 12 12"><path d="M1.5 6.5 L4.5 9.5 L10.5 2.5" fill="none" stroke="var(--red)" stroke-width="2"/></svg>Catering &amp; Equipment Hire</li>
  </ul>

  <div class="brands">
    <p class="partner partner--grill">Grill Yard</p>
    <p class="partner partner--wraps">Condor Wraps</p>
    <p class="partner partner--pie">Tam Lok Ret</p>
    <p class="partner partner--reef">Reefies</p>
    <p class="partner partner--lulu">Bova Lulu</p>
    <p class="partner partner--fine">Bova Fine</p>
    <p class="partner partner--loft">Bova Oven Loft</p>
    <div class="cert-badge" role="img" aria-label="Quality assurance certification badge"></div>
  </div>

  <div class="back-footer">
    <p class="back-footer__owned">100% PNG OWNED</p>
    <p class="back-footer__web">www.vnq-sample.com.pg</p>
  </div>
</section>

</body>
</html>
```